Label design for Japanese healthy drink

We need new label design to give our product a new look. This is Amazake, traditional Japanese drink made out of fermented rice. This is nutrition packed drink and target audience is health conscious people. We want something simple and healthy. The attached photo is current label (for the size reference only) and food pouch the label will be attached. Please don't use anything on the label in the picture.

Target Market(s)

health conscious people (30s - 50s)

Requirements
Must have
• "Amazake"
Should not have
• too much color, picture of rice or sake

```html
<!DOCTYPE html>
<html lang="en">
<head>
<meta charset="utf-8">
<title>Amazake Label</title>
<link rel="stylesheet" href="https://fonts.googleapis.com/css2?family=Noto+Sans+JP:wght@700&display=swap">
<style>
  :root {
    --backdrop: #d4b790;
    --label-pink: #d87f84;
    --leaf-pink: #e9a5a9;
    --white: #ffffff;
  }
  * { margin: 0; padding: 0; box-sizing: border-box; }
  html, body {
    width: 1200px;
    height: 675px;
    overflow: hidden;
    background: var(--backdrop);
  }
  .canvas {
    position: relative;
    width: 1200px;
    height: 675px;
    background: var(--backdrop);
  }
  .label {
    position: absolute;
    left: 370px;
    top: 117.5px;
    width: 460px;
    height: 440px;
    transform: scale(1.12);
    transform-origin: center center;
    font-family: "Noto Sans JP", sans-serif;
    font-weight: 700;
  }
  .label-shape {
    position: absolute;
    inset: 0;
    width: 460px;
    height: 440px;
  }
  .badge {
    position: absolute;
    left: 38px;
    top: 52px;
    padding: 0 12px;
    height: 28px;
    background: var(--white);
    color: var(--label-pink);
    font-size: 15px;
    letter-spacing: 0.5px;
    line-height: 28px;
  }
  .name-kanji {
    position: absolute;
    left: 66px;
    top: 100px;
    color: var(--white);
    font-size: 84px;
    line-height: 1;
  }
  .name-latin {
    position: absolute;
    left: 30px;
    top: 194px;
    width: 400px;
    text-align: center;
    color: var(--white);
    font-size: 80px;
    font-weight: 700;
    line-height: 1.1;
  }
  .tagline {
    position: absolute;
    right: 34px;
    top: 312px;
    text-align: left;
    color: var(--white);
    font-size: 17px;
    line-height: 1.35;
    text-transform: uppercase;
  }
</style>
</head>
<body>
  <main class="canvas">
    <section class="label">
      <svg class="label-shape" viewBox="0 0 460 440" xmlns="http://www.w3.org/2000/svg">
        <rect class="label-body" x="0" y="0" width="460" height="440" rx="24" fill="var(--label-pink)"/>
        <g role="img" aria-label="Decorative stylised leaf motif">
          <rect x="292" y="40" width="110" height="138" rx="12" fill="var(--leaf-pink)" opacity="0.55"/>
          <rect x="40" y="304" width="140" height="100" rx="12" fill="var(--leaf-pink)" opacity="0.55"/>
        </g>
        <rect class="label-frame" x="14" y="14" width="432" height="412" rx="16" fill="none" stroke="var(--white)" stroke-width="3"/>
      </svg>
      <div class="badge">NUTRITION-PACKED</div>
      <div class="name-kanji" lang="ja">甘酒</div>
      <h1 class="name-latin">Amazake</h1>
      <p class="tagline">Traditional Japanese<br>Fermented Rice Drink</p>
    </section>
  </main>
</body>
</html>
```